Illustration For Couples Game - Fun, Edgy, Smart Design

This is a game for couples that is focused on helping them connect on every level... emotional, mental, spiritual, physical, etc. This image is for the back of the cards. I attached the front and it would be awesome if your design for the back worked with the front. If you don't think your idea will work with the front, I am open to a new idea for a different front.

Target Market(s)

middle class women and men from 25-55

Industry/Entity Type

Online Store

Colors
e34297
b768aa
ec1f27
a54499
e667a6
f04a50

Requirements
Must have
• The background needs to be black. For the coloring, red, white, pink, purple are all great. I don't think colors outside of that will work very well but if you feel inspired with other colors I am somewhat open to other colors. Please have the title "Tender Tricks" then "For Couples" as more of a subtitle. Something that is slightly italic and has some shading or outlining might be great, just so that it looks very professional. The dimensions should be 5 inches tall and 3.5 inches wide (sorry not sure about CM). **Also, please have only CMYK designs, thank you!**
Nice to have
• Smart and creative designs that make people think and have depth is great. I actually ran another contest on another site and narrowed down to a few ideas.
• -I like the image of the heart as a lock with a key unlocking it.
• -Also a light bulb shaped as a heart that is turned on
• -Dandelion seeds with hearts attached to them (see example)
• I am open to other images but I know I like these three for sure.
Should not have
• Not overtly sexual since this has more of an emphasis on emotional intimacy than physical. We have found overtly sexual confuses people.

```html
<!DOCTYPE html>
<html lang="en">
<head>
<meta charset="utf-8">
<title>Tender Tricks for Couples – Card Back</title>
<link rel="stylesheet" href="https://fonts.googleapis.com/css2?family=Great+Vibes&display=swap">
<style>
  :root {
    --page-bg: #f4f5f7;
    --card-black: #050505;
    --band-red: #e0143c;
    --band-deep: #8a0c26;
    --heart-pink: #e03289;
    --heart-rose: #e6659a;
    --bubble-mauve: #cc5f9c;
    --dot-lilac: #c872b8;
    --title-pink: #e0287f;
  }
  html, body {
    margin: 0;
    width: 1200px;
    height: 1200px;
    overflow: hidden;
    background: var(--page-bg);
  }
  .canvas {
    position: relative;
    width: 1200px;
    height: 1200px;
  }
  .card-back {
    position: absolute;
    left: 260px;
    top: 118px;
    width: 676px;
    height: 966px;
    display: block;
  }
  .title-script {
    font-family: "Great Vibes", cursive;
    fill: var(--title-pink);
  }
</style>
</head>
<body>
<main class="canvas">
  <svg class="card-back" viewBox="0 0 845 1208" xmlns="http://www.w3.org/2000/svg" aria-label="Tender Tricks for Couples card back">
    <defs>
      <linearGradient id="knot-tone" x1="0" y1="0" x2="0" y2="1">
        <stop offset="0%" stop-color="#e0143c"/>
        <stop offset="100%" stop-color="#b8102f"/>
      </linearGradient>
      <clipPath id="card-clip"><rect width="845" height="1208"/></clipPath>
    </defs>

    <g clip-path="url(#card-clip)">
      <rect class="card-bg" width="845" height="1208" fill="var(--card-black)"/>

      <!-- diagonal bands -->
      <g class="corner-bands" fill="var(--band-red)">
        <polygon points="0,250 290,0 330,0 0,290"/>
        <polygon points="0,80 95,0 140,0 0,115"/>
        <polygon points="845,250 555,0 515,0 845,290"/>
        <polygon points="845,80 750,0 705,0 845,115"/>
        <polygon points="0,958 290,1208 330,1208 0,918"/>
        <polygon points="0,1128 95,1208 140,1208 0,1093"/>
        <polygon points="845,958 555,1208 515,1208 845,918"/>
        <polygon points="845,1128 750,1208 705,1208 845,1093"/>
      </g>

      <!-- ornamental knot hearts (placeholders) -->
      <path class="knot-heart knot-heart--top" role="img"
            aria-label="Interlaced red knot heart ornament, point upward, with a small pink heart at its centre"
            d="M423,13 L610,200 C690,280 650,408 540,408 C480,408 440,380 423,352 C406,380 366,408 306,408 C196,408 156,280 236,200 Z"
            fill="url(#knot-tone)"/>
      <path class="knot-heart knot-heart--bottom" role="img"
            aria-label="Interlaced red knot heart ornament, point downward, with a small pink heart at its centre"
            transform="translate(0,1211) scale(1,-1)"
            d="M423,13 L610,200 C690,280 650,408 540,408 C480,408 440,380 423,352 C406,380 366,408 306,408 C196,408 156,280 236,200 Z"
            fill="url(#knot-tone)"/>

      <!-- side half hearts -->
      <path class="side-heart side-heart--left" d="M0,323 L70,403 A40,40 0 0 1 0,473 Z" fill="var(--heart-rose)"/>
      <path class="side-heart side-heart--right" d="M845,323 L775,403 A40,40 0 0 0 845,473 Z" fill="var(--heart-pink)"/>

      <!-- small twin-tone hearts -->
      <g class="mini-heart" transform="translate(132,553)">
        <path d="M0,-15 C-10,-33 -38,-28 -38,-5 C-38,12 -15,28 0,40 Z" fill="var(--heart-rose)"/>
        <path d="M0,-15 C10,-33 38,-28 38,-5 C38,12 15,28 0,40 Z" fill="var(--heart-pink)"/>
      </g>
      <g class="mini-heart" transform="translate(725,553)">
        <path d="M0,-15 C-10,-33 -38,-28 -38,-5 C-38,12 -15,28 0,40 Z" fill="var(--heart-pink)"/>
        <path d="M0,-15 C10,-33 38,-28 38,-5 C38,12 15,28 0,40 Z" fill="var(--heart-rose)"/>
      </g>

      <!-- speech bubbles with hearts -->
      <g class="chat-bubble chat-bubble--left">
        <path d="M0,703 H180 V856 H110 V911 L40,856 H0 Z" fill="var(--band-red)"/>
        <path d="M72,828 L25,780 A27,27 0 0 1 72,745 A27,27 0 0 1 120,780 Z" fill="var(--card-black)"/>
      </g>
      <g class="chat-bubble chat-bubble--right">
        <path d="M672,703 H845 V856 H810 L745,911 V856 H672 Z" fill="var(--bubble-mauve)"/>
        <path d="M780,828 L733,780 A27,27 0 0 1 780,745 A27,27 0 0 1 828,780 Z" fill="var(--card-black)"/>
      </g>

      <!-- confetti dots -->
      <g class="confetti">
        <circle cx="115" cy="287" r="7" fill="var(--dot-lilac)"/>
        <circle cx="720" cy="226" r="7" fill="var(--dot-lilac)"/>
        <circle cx="703" cy="278" r="8" fill="var(--band-red)"/>
        <circle cx="760" cy="317" r="4" fill="var(--dot-lilac)"/>
        <circle cx="180" cy="380" r="4" fill="var(--dot-lilac)"/>
        <circle cx="678" cy="363" r="4" fill="var(--dot-lilac)"/>
        <circle cx="728" cy="413" r="4" fill="var(--band-red)"/>
        <circle cx="328" cy="428" r="4" fill="var(--dot-lilac)"/>
        <circle cx="28" cy="512" r="4" fill="var(--band-red)"/>
        <circle cx="62" cy="597" r="4" fill="var(--dot-lilac)"/>
        <circle cx="189" cy="627" r="8" fill="var(--band-red)"/>
        <circle cx="800" cy="608" r="4" fill="var(--dot-lilac)"/>
        <circle cx="732" cy="647" r="4" fill="var(--band-red)"/>
        <circle cx="617" cy="745" r="4" fill="var(--band-red)"/>
        <circle cx="311" cy="768" r="4" fill="var(--dot-lilac)"/>
        <circle cx="526" cy="760" r="4" fill="var(--dot-lilac)"/>
        <circle cx="54" cy="928" r="4" fill="var(--dot-lilac)"/>
        <circle cx="689" cy="923" r="8" fill="var(--dot-lilac)"/>
        <circle cx="166" cy="961" r="8" fill="var(--dot-lilac)"/>
        <circle cx="787" cy="944" r="4" fill="var(--dot-lilac)"/>
        <circle cx="180" cy="1023" r="8" fill="var(--dot-lilac)"/>
        <circle cx="735" cy="983" r="4" fill="var(--band-red)"/>
        <circle cx="668" cy="1018" r="4" fill="var(--dot-lilac)"/>
      </g>

      <!-- title -->
      <g class="title-block">
        <text class="title-script title-main" x="428" y="540" text-anchor="middle" font-size="104"
              textLength="470" lengthAdjust="spacingAndGlyphs">Tender Tricks</text>
        <text class="title-script title-for" x="420" y="612" text-anchor="middle" font-size="64">for</text>
        <text class="title-script title-sub" x="438" y="712" text-anchor="middle" font-size="150"
              textLength="400" lengthAdjust="spacingAndGlyphs">Couples</text>
      </g>
    </g>
  </svg>
</main>
</body>
</html>
```